Tolvane Air Center needs a new upscale business card design for our high end aircraft hangar complex

Tolvane Air Center (TAC) is a large, upscale jet hangar complex in the US housing expensive aircraft. We need a new business card design, using our current logo. We will be attending a industry convention and need a card design that will stand out and be remembered by aircraft owners and private pilots.

Target Market(s)

Aircraft pilots or owners looking for a new upscale hangar

Industry/Entity Type

Airport

I like to use very heavy card stock, 400#, double sided. Square, no rounded edges please.

Colors
3276b5
0255a3
85abd2

Requirements
Must have
• An expensive, classy design, vivid colors.
Nice to have
• Needs to look very expensive and classy, and have some "pop". Designer must be able to download or copy my current typeface or fonts.
• One card side might be black with the "Logo and Tolvane Air Center Double line image in blue (or try gold, or glossy black), and perhaps have a grayed out "R470 jet silhouette". The other card side would have our contact info, and perhaps the "TAC Logo only". I'd like my contact info 'stacked', not in a paragraph format.
Should not have
• Should not look "too busy". Having a double-sided card will help.

```html
<!DOCTYPE html>
<html lang="en">
<head>
<meta charset="utf-8">
<title>Tolvane Air Center – Business Card</title>
<link rel="stylesheet" href="https://fonts.googleapis.com/css2?family=Saira:wght@700&family=Roboto:wght@400;700&family=Open+Sans:wght@400;700&display=swap">
<style>
  :root {
    --card-black: #0a0a0f;
    --brand-blue: #0a56a3;
    --brand-mid: #3276b5;
    --brand-deep: #0255a3;
    --brand-light: #85abd2;
    --panel-white: #f4f5f5;
    --name-ink: #2b2b33;
    --white: #ffffff;
  }
  * { margin: 0; padding: 0; box-sizing: border-box; }
  html, body { width: 1200px; height: 338px; overflow: hidden; background: var(--white); }
  .sheet { position: relative; width: 1200px; height: 338px; }

  .card { position: absolute; top: 0; width: 592px; height: 338px; background: var(--card-black); overflow: hidden; }
  .card--front { left: 0; }
  .card--back { left: 608px; }

  /* Front */
  .front-mark {
    position: absolute; left: 0; right: 0; top: 58px; text-align: center;
    font-family: "Saira", sans-serif; font-weight: 700; font-size: 118px; line-height: 1;
    color: var(--brand-deep); letter-spacing: 6px;
  }
  .front-name {
    position: absolute; left: 0; right: 0; top: 212px; text-align: center;
    font-family: "Saira", sans-serif; font-weight: 700; font-size: 44px; line-height: 1;
    color: var(--brand-deep); text-transform: uppercase; letter-spacing: 1px;
  }
  .contact-band {
    position: absolute; left: 0; bottom: 0; width: 100%; height: 56px;
    background: var(--brand-blue);
    display: flex; align-items: center; gap: 18px; padding-left: 22px;
  }
  .contact-band .contact-item {
    display: flex; align-items: center; gap: 7px;
    font-family: "Open Sans", sans-serif; font-size: 14.5px; color: var(--white);
  }
  .icon { width: 20px; height: 20px; flex: none; }
  .contact-band .icon circle.bg { fill: var(--white); }
  .contact-band .icon .glyph { fill: var(--brand-blue); stroke: var(--brand-blue); }

  /* Back */
  .info-panel { position: absolute; inset: 0; width: 592px; height: 338px; }
  .info-panel polygon.panel { fill: var(--panel-white); }
  .info-panel polygon.name-band { fill: var(--brand-mid); }
  .info-panel polygon.band-fold { fill: var(--brand-deep); }

  .back-mark {
    position: absolute; left: 42px; width: 228px; top: 108px; text-align: center;
    font-family: "Saira", sans-serif; font-weight: 700; font-size: 84px; line-height: 1;
    color: var(--brand-deep); letter-spacing: 4px;
  }
  .jet-silhouette {
    position: absolute; left: 44px; top: 210px; width: 226px; height: 56px;
    background: radial-gradient(ellipse at 50% 60%, #4a4a50 0%, #2a2a2f 45%, rgba(10,10,15,0) 75%);
  }
  .person-name {
    position: absolute; left: 330px; top: 86px;
    font-family: "Roboto", sans-serif; font-weight: 700; font-size: 30px; line-height: 1;
    color: var(--name-ink); letter-spacing: 1px;
  }
  .person-role {
    position: absolute; left: 387px; top: 133px;
    font-family: "Roboto", sans-serif; font-weight: 400; font-size: 14px;
    color: var(--name-ink); letter-spacing: 3px;
  }
  .contact-stack { position: absolute; left: 368px; top: 204px; list-style: none; }
  .contact-stack .contact-item {
    display: flex; align-items: center; gap: 9px; height: 24px; margin-bottom: 9px;
    font-family: "Open Sans", sans-serif; font-weight: 700; font-size: 13.5px; color: var(--brand-blue);
  }
  .contact-stack .icon { width: 24px; height: 24px; }
  .contact-stack .icon circle.bg { fill: var(--brand-blue); }
  .contact-stack .icon .glyph { fill: var(--white); stroke: var(--white); }
</style>
</head>
<body>
<main class="sheet">

  <section class="card card--front" aria-label="Card front">
    <div class="front-mark">TAC</div>
    <div class="front-name">Tolvane Air Center</div>

    <div class="contact-band">
      <div class="contact-item">
        <svg class="icon" viewBox="0 0 20 20" aria-hidden="true">
          <circle class="bg" cx="10" cy="10" r="10"/>
          <g class="glyph" fill="none" stroke-width="1.4">
            <circle cx="10" cy="10" r="5.5" style="fill:none"/>
            <line x1="4.5" y1="10" x2="15.5" y2="10"/>
            <ellipse cx="10" cy="10" rx="2.4" ry="5.5" style="fill:none"/>
          </g>
        </svg>
        <span>www.your-company.com</span>
      </div>
      <div class="contact-item">
        <svg class="icon" viewBox="0 0 20 20" aria-hidden="true">
          <circle class="bg" cx="10" cy="10" r="10"/>
          <path class="glyph" stroke="none" d="M6.3 5.2l1.9-.4 1.1 2.6-1.3 1c.6 1.3 1.5 2.2 2.8 2.8l1-1.3 2.6 1.1-.4 1.9c-.2.6-.8 1-1.5.9-3.7-.5-6.6-3.4-7.1-7.1-.1-.7.3-1.3.9-1.5z"/>
        </svg>
        <span>+1 123-456-7890</span>
      </div>
      <div class="contact-item">
        <svg class="icon" viewBox="0 0 20 20" aria-hidden="true">
          <circle class="bg" cx="10" cy="10" r="10"/>
          <rect class="glyph" x="5" y="6.5" width="10" height="7" stroke="none"/>
          <path d="M5.4 7l4.6 3.6L14.6 7" fill="none" stroke="#ffffff" stroke-width="1"/>
        </svg>
        <span>contacts@company.com</span>
      </div>
    </div>
  </section>

  <section class="card card--back" aria-label="Card back">
    <svg class="info-panel" viewBox="0 0 592 338" aria-hidden="true">
      <polygon class="panel" points="420,0 592,0 592,338 270,338"/>
      <polygon class="name-band" points="306,80 592,80 592,126 306,126"/>
      <polygon class="band-fold" points="306,126 356,126 348,166"/>
    </svg>

    <div class="back-mark">TAC</div>
    <div class="jet-silhouette" role="img" aria-label="Grey front-view silhouette of an R470 business jet"></div>

    <div class="person-name">Your Name</div>
    <div class="person-role">Designation</div>

    <ul class="contact-stack">
      <li class="contact-item">
        <svg class="icon" viewBox="0 0 20 20" aria-hidden="true">
          <circle class="bg" cx="10" cy="10" r="10"/>
          <path class="glyph" stroke="none" d="M6.3 5.2l1.9-.4 1.1 2.6-1.3 1c.6 1.3 1.5 2.2 2.8 2.8l1-1.3 2.6 1.1-.4 1.9c-.2.6-.8 1-1.5.9-3.7-.5-6.6-3.4-7.1-7.1-.1-.7.3-1.3.9-1.5z"/>
        </svg>
        <span>+1 123-456-7890</span>
      </li>
      <li class="contact-item">
        <svg class="icon" viewBox="0 0 20 20" aria-hidden="true">
          <circle class="bg" cx="10" cy="10" r="10"/>
          <g class="glyph" fill="none" stroke-width="1.4">
            <circle cx="10" cy="10" r="5.5" style="fill:none"/>
            <line x1="4.5" y1="10" x2="15.5" y2="10"/>
            <ellipse cx="10" cy="10" rx="2.4" ry="5.5" style="fill:none"/>
          </g>
        </svg>
        <span>www.your-company.com</span>
      </li>
      <li class="contact-item">
        <svg class="icon" viewBox="0 0 20 20" aria-hidden="true">
          <circle class="bg" cx="10" cy="10" r="10"/>
          <rect class="glyph" x="5" y="6.5" width="10" height="7" stroke="none"/>
          <path d="M5.4 7l4.6 3.6L14.6 7" fill="none" stroke="#0a56a3" stroke-width="1"/>
        </svg>
        <span>contacts@company.com</span>
      </li>
    </ul>
  </section>

</main>
</body>
</html>
```